Leadership Conference Graphic Design Image

The Theme of our Conference is "Navigating Change. Driving Success." Attached is an AI example - What we are looking for is something along the lines of this image, but with realistic roads, a realistic semi truck (without being able to tell the make of the semi truck) and with the semi truck leaving dark skies and heading towards positive sunnier type skies. Please don't use the "Pinecrest Haulers Guild Yearly Convention" verbiage - Our event is called "Leadership Conference and Vendor Showcase". I've also attached our logo which we would like on the image as well - And we would like both vertical and horizontal designs. We will be using this on our stage and in printed materials.

```html
<!DOCTYPE html>
<html lang="en">
<head>
<meta charset="utf-8">
<title>Navigating Change. Driving Success.</title>
<link rel="stylesheet" href="https://fonts.googleapis.com/css2?family=Inter+Tight:wght@400;500;800&display=swap">
<style>
  :root {
    --brand-blue: #0a4c9c;
    --sky-top: #8fb3d6;
    --sky-mid: #dfe6ea;
    --cloud-grey: #8c9096;
    --horizon-warm: #f1dcb4;
    --land: #8c7a55;
    --road: #3a3836;
    --white: #ffffff;
  }
  * { margin: 0; padding: 0; box-sizing: border-box; }
  html, body { width: 675px; height: 1200px; overflow: hidden; }
  body { font-family: "Inter Tight", Arial, sans-serif; }

  .poster {
    position: relative;
    width: 675px;
    height: 1200px;
    overflow: hidden;
  }

  .scene-photo {
    position: absolute;
    inset: 0;
    background:
      radial-gradient(ellipse 60% 30% at 15% 50%, rgba(255,244,214,0.95), rgba(255,244,214,0) 70%),
      radial-gradient(ellipse 55% 45% at 85% 35%, rgba(110,112,118,0.85), rgba(110,112,118,0) 75%),
      linear-gradient(180deg,
        var(--sky-top) 0%,
        var(--sky-mid) 30%,
        #e9e2d2 48%,
        var(--horizon-warm) 55%,
        #9a9288 62%,
        #6f6a60 66%,
        var(--land) 69%,
        #5a5550 73%,
        var(--road) 82%,
        #2a2725 100%);
  }

  .event-kicker {
    position: absolute;
    left: 41px;
    top: 121px;
    font-size: 16.5px;
    font-weight: 500;
    letter-spacing: -0.2px;
    color: var(--brand-blue);
  }

  .kicker-rule {
    position: absolute;
    left: 41px;
    top: 172px;
    width: 130px;
    height: 2px;
    background: var(--brand-blue);
  }

  .theme-headline {
    position: absolute;
    left: 38px;
    top: 222px;
    color: var(--brand-blue);
    font-size: 93px;
    line-height: 83px;
    letter-spacing: -2px;
  }
  .theme-headline .line { display: block; }
  .theme-headline .strong { font-weight: 800; }
  .theme-headline .light { font-weight: 400; }

  .org-name {
    position: absolute;
    left: 41px;
    top: 1060px;
    color: var(--white);
    font-weight: 800;
    font-size: 22px;
    line-height: 26px;
    letter-spacing: 0.3px;
    text-transform: uppercase;
  }
</style>
</head>
<body>
  <main class="poster">
    <div class="scene-photo" role="img" aria-label="Photo of a semi truck on an open desert highway with mountains, driving from dark rain clouds toward a bright sunny sky"></div>

    <p class="event-kicker">Leadership Conference and Vendor Showcase Present:</p>
    <div class="kicker-rule"></div>

    <h1 class="theme-headline">
      <span class="line strong">Navigating</span>
      <span class="line strong">Change.</span>
      <span class="line light">Driving</span>
      <span class="line light">Success.</span>
    </h1>

    <p class="org-name">Pinecrest<br>Haulers Guild</p>
  </main>
</body>
</html>
```